Mardi Gras Ball 2014

We're looking to create an 8 1/2" x11" print design using certain elements that we provide.

This is for an invitation/program cover for a Mardi Gras Ball - so the design has to have a classy look using a set number of colors - GOLD, PURPLE, GREEN - white can also be used as accent or boarder elements.

Please use the file KPLOR 2014 for inspiration and direction. The design MUST connect to that file.

The final design should cause a WOW! factor and play off / or be a companion to design we will upload. (see files)

Requirements
Must have
• Dimension size 8 1/2'' x 11'' (bleed to the end)
Port Elvany Seal to remain (can be small)
A Mardi Gras Mask or person in mask behind front elements which should use transparency
Event location, date, time
Files appropriate for printing - with a semi-transparent object in file
Nice to have
• Key elements like shown on the KPLOR 2014 file
Purple as a key color - either as background or like feathers on picture
10th Annual must show nicely
FONTS: New Century Schoolbook LT and Spinwerad

```html
<!DOCTYPE html>
<html lang="en">
<head>
<meta charset="utf-8">
<title>10th Annual Mardi Gras Ball</title>
<link rel="stylesheet" href="https://fonts.googleapis.com/css2?family=Fredoka:wght@600&family=Old+Standard+TT:wght@400;700&family=Lobster&family=Tinos&display=swap">
<style>
  :root {
    --purple: #4a1f6e;
    --purple-deep: #2a0f45;
    --green: #3f9a35;
    --green-bright: #5fb04a;
    --gold: #f5e43a;
    --gold-deep: #b8892a;
    --parchment: #ecdcb6;
    --parchment-edge: #cdb486;
    --ink: #3a2a1c;
    --violet-text: #5a2b86;
    --white: #ffffff;
  }
  html, body { margin: 0; padding: 0; overflow: hidden; background: #1a0d24; }
  .invitation {
    position: relative;
    width: 927px;
    height: 1200px;
    overflow: hidden;
    background: var(--purple-deep);
  }
  .stripe-band {
    position: absolute;
    left: 0;
    width: 927px;
    height: 78px;
    background: repeating-linear-gradient(90deg,
      var(--purple) 0 70px, var(--green) 70px 140px);
  }
  .stripe-band--top { top: 0; }
  .stripe-band--bottom { bottom: 0; height: 72px; }
  .festive-backdrop {
    position: absolute;
    top: 78px; left: 0;
    width: 927px; height: 1050px;
    background:
      radial-gradient(ellipse 210px 330px at 180px 360px, #e8e2d8 0%, #cfc3b4 55%, rgba(120,60,130,0) 100%),
      radial-gradient(circle at 820px 700px, rgba(206,170,60,.75), rgba(0,0,0,0) 260px),
      radial-gradient(circle at 150px 880px, rgba(150,110,190,.8), rgba(0,0,0,0) 260px),
      radial-gradient(circle at 800px 250px, rgba(60,140,60,.7), rgba(0,0,0,0) 280px),
      linear-gradient(160deg, #3b2a1a 0%, #4a2a5c 35%, #2f5a2a 65%, #5a3f1c 100%);
  }
  .association-name {
    position: absolute;
    top: 148px; left: 372px; width: 570px;
    margin: 0;
    text-align: center;
    font-family: "Fredoka", "Arial Rounded MT Bold", sans-serif;
    font-weight: 600;
    font-size: 44px;
    line-height: 60px;
    color: var(--gold);
    text-shadow: 2px 3px 4px rgba(0,0,0,.6);
  }
  .parchment {
    position: absolute;
    top: 285px; left: 372px;
    width: 506px; height: 795px;
    background:
      radial-gradient(ellipse at 50% 45%, #f3e6c6 0%, var(--parchment) 60%, var(--parchment-edge) 100%);
    clip-path: polygon(0 1%, 8% 0, 22% 1.2%, 40% 0.3%, 58% 1%, 76% 0, 92% 1.1%, 100% 0.4%,
      99.2% 20%, 100% 42%, 99% 63%, 100% 82%, 99.4% 100%, 80% 99%, 60% 100%, 38% 99.2%,
      18% 100%, 1% 99.3%, 0.6% 78%, 0 55%, 1% 33%);
    box-shadow: 0 0 30px rgba(0,0,0,.5);
  }
  .invite-line {
    position: absolute;
    top: 306px; left: 372px; width: 506px;
    margin: 0;
    text-align: center;
    font-family: "Tinos", "Times New Roman", serif;
    font-size: 22px;
    color: var(--ink);
  }
  .edition-number {
    position: absolute;
    top: 315px; left: 425px;
    margin: 0;
    font-family: "Old Standard TT", "Century Schoolbook", serif;
    font-weight: 700;
    font-size: 340px;
    line-height: 1;
    letter-spacing: -8px;
    color: var(--green-bright);
    -webkit-text-stroke: 3px var(--white);
    text-shadow: 3px 4px 0 #2f6e2a, 6px 8px 10px rgba(0,0,0,.35);
  }
  .edition-suffix {
    position: absolute;
    top: 370px; left: 762px;
    margin: 0;
    font-family: "Old Standard TT", "Century Schoolbook", serif;
    font-weight: 700;
    font-size: 70px;
    line-height: 1;
    color: var(--green-bright);
    -webkit-text-stroke: 1.5px var(--white);
    text-shadow: 2px 3px 0 #2f6e2a;
  }
  .edition-label {
    position: absolute;
    top: 650px; left: 505px;
    margin: 0;
    font-family: "Lobster", cursive;
    font-size: 66px;
    line-height: 1;
    color: var(--violet-text);
  }
  .event-title {
    position: absolute;
    top: 720px; left: 372px; width: 506px;
    margin: 0;
    text-align: center;
    font-family: "Old Standard TT", "Century Schoolbook", serif;
    font-weight: 400;
    font-size: 58px;
    line-height: 1;
    color: var(--violet-text);
  }
  .event-details {
    position: absolute;
    left: 402px; top: 795px;
    margin: 0;
    font-family: "Tinos", "Times New Roman", serif;
    font-size: 21px;
    line-height: 25px;
    color: var(--ink);
  }
  .detail-row { display: flex; margin-bottom: 37px; }
  .detail-row dt { width: 82px; }
  .detail-row dd { margin: 0; }
  .dress-code {
    position: absolute;
    top: 838px; right: 594px;
    margin: 0;
    text-align: right;
    font-family: "Tinos", "Times New Roman", serif;
    font-size: 21px;
    line-height: 27px;
    color: var(--white);
    text-shadow: 1px 1px 3px rgba(0,0,0,.8);
  }
  .school-mark {
    position: absolute;
    left: 62px; top: 1052px;
    display: flex; align-items: center; gap: 12px;
    font-family: "Tinos", "Times New Roman", serif;
    font-size: 21px;
    color: var(--white);
  }
  .school-mark-circle {
    width: 100px; height: 100px;
    border-radius: 50%;
    background: var(--gold-deep);
  }
</style>
</head>
<body>
<main class="invitation">
  <div class="stripe-band stripe-band--top"></div>
  <div class="festive-backdrop" role="img" aria-label="Photograph of a white Mardi Gras mask with purple and gold glitter among beads, feathers and ribbons"></div>

  <h1 class="association-name">The Association of<br>Port Elvany Alumni</h1>

  <div class="parchment"></div>
  <p class="invite-line">requests your presence at our</p>
  <p class="edition-number">10</p>
  <p class="edition-suffix">th</p>
  <p class="edition-label">Annual</p>
  <h2 class="event-title">Mardi Gras Ball</h2>

  <dl class="event-details">
    <div class="detail-row"><dt>WHEN:</dt><dd>Saturday, Feb. 22, 2014<br>7pm–12am</dd></div>
    <div class="detail-row"><dt>WHERE:</dt><dd>Harbor Crest<br>Convention Center<br>1400 Lantern Row Concourse<br>MARLOW CITY, GEORGIA</dd></div>
  </dl>

  <p class="dress-code">A Semi Formal Affair<br>Tea Length or Formal Dresses<br>Tuxedo, Dark Suits and Ties<br>NO HATS ALLOWED<br>Cost: $75.00</p>

  <div class="school-mark">
    <span class="school-mark-circle"></span>
    <span class="school-mark-name">Port Elvany High</span>
  </div>

  <div class="stripe-band stripe-band--bottom"></div>
</main>
</body>
</html>
```